Email Signiture and letterhead design

we are looking for a modern business design to incorporate our logo and qel certification plus social icons for Vorlant, Pelmora, and zandoro
they must include our UK vat and also company registration as text but I can fill these out. Email signature to have a link/icon to our webshop www.trexolan.co.uk

Target Market(s)

All

Font styles to use
Serif
Sans Serif

Requirements
Must have
• Address, tel, email , web details incorperated
Nice to have
• a professional looking letter head and email signiture, Email signature to have a link/icon to our webshop www.trexolan.co.uk

```html
<!DOCTYPE html>
<html lang="en">
<head>
<meta charset="utf-8">
<title>Trexolan Email Signature</title>
<link rel="stylesheet" href="https://fonts.googleapis.com/css2?family=Roboto:wght@400;500;700&display=swap">
<style>
  :root {
    --brand-red: #e5202a;
    --ink: #2b2b2d;
    --page: #ececee;
    --card: #ffffff;
  }
  * { box-sizing: border-box; margin: 0; padding: 0; }
  html, body {
    width: 1200px; height: 906px; overflow: hidden;
    background: var(--page);
    font-family: "Roboto", Arial, sans-serif;
    color: var(--ink);
  }
  .signature {
    position: absolute; left: 40px; top: 270px;
    width: 1120px; height: 366px;
    background: var(--card);
  }
  .brand {
    position: absolute; left: 0; top: 0; width: 595px; height: 366px;
  }
  .brand-mark {
    position: absolute; left: 0; right: 0; top: 118px;
    display: flex; align-items: center; justify-content: center; gap: 14px;
  }
  .brand-dot {
    width: 44px; height: 44px; border-radius: 50%;
    background: var(--brand-red);
    flex: none;
  }
  .brand-name {
    font-size: 30px; font-weight: 700; color: var(--ink);
    letter-spacing: 0.5px; white-space: nowrap;
  }
  .social {
    position: absolute; left: 0; right: 0; top: 280px;
    display: flex; justify-content: center; gap: 18px;
    list-style: none;
  }
  .social-item {
    display: flex; align-items: center; gap: 6px;
    font-size: 15px; font-weight: 500; color: var(--brand-red);
  }
  .social-item::before {
    content: ""; width: 14px; height: 14px; border-radius: 50%;
    background: var(--brand-red);
  }
  .divider {
    position: absolute; left: 595px; top: 35px;
    width: 3px; height: 304px; background: var(--brand-red);
  }
  .details {
    position: absolute; left: 624px; top: 30px;
  }
  .person-name {
    font-size: 34px; font-weight: 700; color: var(--brand-red);
    line-height: 40px;
  }
  .person-role {
    font-size: 23px; line-height: 28px; margin-top: 6px;
  }
  .address {
    font-style: normal; font-size: 23px; line-height: 38px;
    margin-top: 28px;
  }
  .contacts {
    list-style: none; margin-top: 22px;
  }
  .contact {
    display: flex; align-items: center; gap: 10px;
    font-size: 23px; height: 38px;
  }
  .contact-icon { width: 26px; height: 26px; flex: none; }
</style>
</head>
<body>
  <section class="signature">
    <div class="brand">
      <div class="brand-mark">
        <span class="brand-dot"></span>
        <span class="brand-name">Trexolan Hubs &amp; Bearings Ltd</span>
      </div>
      <ul class="social">
        <li class="social-item">Vorlant</li>
        <li class="social-item">Pelmora</li>
        <li class="social-item">zandoro</li>
      </ul>
    </div>

    <div class="divider"></div>

    <div class="details">
      <h1 class="person-name">ALDOUS FENWICK</h1>
      <p class="person-role">Managing Director</p>
      <address class="address">
        Calder Row East,<br>
        Brinsworth, Manchester, M91 4QT
      </address>
      <ul class="contacts">
        <li class="contact">
          <svg class="contact-icon" viewBox="0 0 26 26" aria-hidden="true">
            <circle cx="13" cy="13" r="13" fill="var(--brand-red)"/>
            <path d="M6 11c0-2 3-3.5 7-3.5s7 1.5 7 3.5l-2.5.6-1-1.6h-7l-1 1.6z" fill="#fff"/>
            <path d="M8.5 12.5h9l1 5.5h-11z" fill="#fff"/>
          </svg>
          <span>+44 (0) 161 555 0192</span>
        </li>
        <li class="contact">
          <svg class="contact-icon" viewBox="0 0 26 26" aria-hidden="true">
            <circle cx="13" cy="13" r="13" fill="var(--brand-red)"/>
            <rect x="6.5" y="8.5" width="13" height="9" rx="1.5" fill="#fff"/>
            <path d="M6.8 9.2 13 14l6.2-4.8" fill="none" stroke="var(--brand-red)" stroke-width="1.4"/>
          </svg>
          <span>info@trexolanmail.com</span>
        </li>
        <li class="contact">
          <svg class="contact-icon" viewBox="0 0 26 26" aria-hidden="true">
            <circle cx="13" cy="13" r="13" fill="var(--brand-red)"/>
            <circle cx="13" cy="13" r="7" fill="none" stroke="#fff" stroke-width="1.6"/>
            <path d="M13 6v14M6 13h14" stroke="#fff" stroke-width="1.4"/>
          </svg>
          <span>www.trexolan.co.uk</span>
        </li>
      </ul>
    </div>
  </section>
</body>
</html>
```